Business Card Design Project

Cyber Security. Company name is brightHarbor.

Industry/Entity Type

Computer Security

Contact Information for Business Card

Gregory Lindqvist
Founder and Chief Hacker

2370 W. Alder Rd.
Suite 514
Chicago, IL 60482
773.555.0196
gregory.lindqvist@brightharbor.example
www.brightharbor.example

```html
<!DOCTYPE html>
<html lang="en">
<head>
<meta charset="utf-8">
<title>brightHarbor — Business Card</title>
<link rel="stylesheet" href="https://fonts.googleapis.com/css2?family=Open+Sans:wght@400&family=Roboto:wght@400;700&display=swap">
<style>
  :root {
    --stage: #e9e6e1;
    --card-dark: #0b0d0f;
    --card-light: #ffffff;
    --ink: #151515;
    --ink-soft: #333333;
    --accent-blue: #2f7fd0;
    --accent-green: #6aa829;
    --logo-dark: #d9dde6;
    --logo-light: #5a6fb8;
  }
  * { box-sizing: border-box; margin: 0; padding: 0; }
  html, body { width: 1200px; height: 900px; overflow: hidden; }
  body {
    background: var(--stage);
    display: flex;
    align-items: center;
    justify-content: center;
    gap: 44px;
    font-family: "Roboto", Arial, sans-serif;
  }
  .card {
    width: 550px;
    height: 315px;
    position: relative;
    box-shadow: 0 10px 28px rgba(0,0,0,0.18);
  }
  .card-front { background: var(--card-dark); }
  .card-back { background: var(--card-light); }

  .wordmark {
    position: absolute;
    display: flex;
    align-items: center;
    gap: 14px;
    font-family: "Open Sans", Arial, sans-serif;
    font-weight: 400;
    letter-spacing: 0.5px;
    white-space: nowrap;
  }
  .wordmark-dot { width: 34px; height: 34px; border-radius: 50%; }
  .card-front .wordmark {
    left: 50%; top: 50%; transform: translate(-50%, -50%);
    font-size: 46px; color: var(--logo-dark);
  }
  .card-front .wordmark-dot { background: var(--logo-dark); }

  .card-back .wordmark {
    left: 50%; top: 132px; transform: translate(-50%, -50%);
    font-size: 42px; color: var(--logo-light);
  }
  .card-back .wordmark-dot { background: var(--logo-light); }

  .holder { position: absolute; right: 30px; top: 26px; text-align: right; }
  .holder-name { font-size: 26px; color: var(--ink); line-height: 1.1; font-weight: 400; }
  .holder-name strong { font-weight: 700; }
  .holder-title { font-size: 14px; color: var(--accent-green); margin-top: 2px; }

  .contacts {
    position: absolute; left: 26px; right: 26px; bottom: 22px;
    display: grid;
    grid-template-columns: auto auto;
    justify-content: space-between;
    align-items: center;
    row-gap: 10px;
    list-style: none; font-size: 12px; line-height: 1.35; color: var(--ink-soft);
  }
  .contact { display: flex; align-items: center; gap: 7px; white-space: nowrap; }
  .contact-label { color: var(--accent-blue); font-weight: 700; }
  .contact svg { width: 20px; height: 20px; flex: none; }
</style>
</head>
<body>
  <section class="card card-front" aria-label="Card front">
    <div class="wordmark"><span class="wordmark-dot"></span><span>brightHarbor</span></div>
  </section>

  <section class="card card-back" aria-label="Card back">
    <div class="holder">
      <p class="holder-name"><strong>Gregory</strong> Lindqvist</p>
      <p class="holder-title">Founder and Chief Hacker</p>
    </div>

    <div class="wordmark"><span class="wordmark-dot"></span><span>brightHarbor</span></div>

    <ul class="contacts">
      <li class="contact">
        <svg viewBox="0 0 20 20" aria-hidden="true"><circle cx="10" cy="10" r="9" fill="none" stroke="#2f7fd0" stroke-width="1.5"/><path d="M10 4.8a3.4 3.4 0 0 0-3.4 3.4c0 2.5 3.4 6.6 3.4 6.6s3.4-4.1 3.4-6.6A3.4 3.4 0 0 0 10 4.8z" fill="#2f7fd0"/><circle cx="10" cy="8.2" r="1.2" fill="#fff"/></svg>
        <span><span class="contact-label">A:</span> 2370 W. Alder Rd., Suite 514<br>Chicago, IL 60482</span>
      </li>
      <li class="contact">
        <svg viewBox="0 0 20 20" aria-hidden="true"><circle cx="10" cy="10" r="9" fill="none" stroke="#2f7fd0" stroke-width="1.5"/><rect x="5.5" y="6.5" width="9" height="7" rx="1" fill="#2f7fd0"/><path d="M5.8 7l4.2 3.2L14.2 7" fill="none" stroke="#fff" stroke-width="1"/></svg>
        <span><span class="contact-label">E:</span> gregory.lindqvist@brightharbor.example</span>
      </li>
      <li class="contact">
        <svg viewBox="0 0 20 20" aria-hidden="true"><circle cx="10" cy="10" r="9" fill="none" stroke="#2f7fd0" stroke-width="1.5"/><path d="M7 5.5c-.8.4-1.3 1.2-1 2.3.7 2.6 2.6 4.5 5.2 5.2 1.1.3 1.9-.2 2.3-1l-1.7-1.3-1 .7c-1.1-.5-2-1.4-2.5-2.5l.7-1z" fill="#2f7fd0"/></svg>
        <span><span class="contact-label">P:</span> (773) 555-0196</span>
      </li>
      <li class="contact">
        <svg viewBox="0 0 20 20" aria-hidden="true"><circle cx="10" cy="10" r="9" fill="none" stroke="#2f7fd0" stroke-width="1.5"/><circle cx="10" cy="10" r="4.6" fill="none" stroke="#2f7fd0" stroke-width="1.2"/><path d="M5.4 10h9.2M10 5.4v9.2" stroke="#2f7fd0" stroke-width="1"/></svg>
        <span><span class="contact-label">W:</span> www.brightharbor.example</span>
      </li>
    </ul>
  </section>
</body>
</html>
```